Independent Statistical Consultant Business Card

I will be going out as an independent statistical consultant and need a business card. I specialize in data analysis and statistics for health care and public health

I am an Licensed Numeric Examiner from the Coastal Metrics Society. Would like to incorporate that logo into the design

The design should be modern with classic colors, convey accuracy, analytic creativity and responsiveness to client needs.

The name of the firm will be simply Tim Halvarsen Numeric Insight Services

To all designers, I want to clarify that the DCred logo and the phrase Licensed Numeric Examiner are not the name of the company nor the focus of the card. They are equivalent to being a Veltrano Qualified Engineer (VQE) but in the area of statistics The name of the firm will be: Tim Halvarsen, Numeric Insight Services. I look forward to your submissions. Thanks. Tim

```html
<!DOCTYPE html>
<html lang="en">
<head>
<meta charset="utf-8">
<title>Tim Halvarsen – Business Card</title>
<link rel="stylesheet" href="https://fonts.googleapis.com/css2?family=Questrial&family=Arimo:wght@400;700&display=swap">
<style>
  :root {
    --backdrop: #2a2a2a;
    --card-white: #ffffff;
    --card-shade: #e9e9ea;
    --brand-blue: #1d56a6;
    --brand-blue-deep: #123e86;
    --brand-blue-light: #7fa6dc;
    --ink-grey: #6d6e70;
    --ink-dark: #4a4b4d;
  }
  * { box-sizing: border-box; margin: 0; padding: 0; }
  html, body {
    width: 1200px; height: 900px; overflow: hidden;
    background: var(--backdrop);
  }
  .canvas {
    width: 1200px; height: 900px;
    display: flex; flex-direction: column;
    align-items: center; justify-content: center; gap: 40px;
  }
  .card {
    position: relative;
    width: 680px; height: 388px;
    border-radius: 26px;
    overflow: hidden;
  }

  /* Back side */
  .card-back {
    background: linear-gradient(135deg, var(--brand-blue) 0%, var(--brand-blue-deep) 100%);
  }
  .card-back .facets { position: absolute; inset: 0; }
  .card-back .back-name {
    position: absolute; left: 128px; top: 150px;
    font-family: "Questrial", sans-serif;
    color: var(--card-white);
    font-size: 64px; letter-spacing: 0.5px; line-height: 1;
  }
  .card-back .back-tagline {
    position: absolute; left: 132px; top: 222px;
    font-family: "Questrial", sans-serif;
    color: var(--brand-blue-light);
    font-size: 19px; letter-spacing: 1.5px; text-transform: uppercase;
  }

  /* Front side */
  .card-front {
    background: linear-gradient(160deg, var(--card-white) 40%, var(--card-shade) 100%);
  }
  .card-front .edge-notch { position: absolute; left: 0; top: 100px; }
  .credential {
    position: absolute; left: 52px; top: 60px;
  }
  .credential .mark {
    display: flex; align-items: center; gap: 8px;
    font-family: "Questrial", sans-serif;
    font-size: 40px; line-height: 1;
    color: var(--brand-blue-deep);
  }
  .credential .mark .dot {
    width: 12px; height: 12px; border-radius: 50%;
    background: var(--brand-blue-deep);
  }
  .credential .caption {
    margin-top: 5px;
    font-family: "Arimo", sans-serif;
    font-size: 10px; color: var(--ink-dark);
  }
  .firm {
    position: absolute; right: 46px; top: 48px; text-align: left;
  }
  .firm .firm-name {
    font-family: "Questrial", sans-serif;
    font-size: 42px; line-height: 1; color: var(--brand-blue);
  }
  .firm .firm-tagline {
    margin-top: 4px;
    font-family: "Questrial", sans-serif;
    font-size: 13px; letter-spacing: 1px; color: var(--ink-grey);
    text-transform: uppercase;
  }
  .divider {
    position: absolute; left: 200px; right: 46px; top: 190px;
    height: 1.5px; background: var(--brand-blue);
  }
  .address {
    position: absolute; right: 46px; top: 206px; text-align: right;
    font-family: "Arimo", sans-serif;
    font-size: 15px; line-height: 1.3; color: var(--ink-grey);
  }
  .person {
    position: absolute; left: 52px; top: 158px;
    font-family: "Arimo", sans-serif;
  }
  .person .person-name {
    font-weight: 700; font-size: 16px; color: var(--brand-blue-deep);
  }
  .person .person-role {
    font-size: 15px; color: var(--ink-grey);
  }
  .contact {
    position: absolute; left: 52px; top: 230px;
    font-family: "Arimo", sans-serif; font-size: 16px; line-height: 1.4;
    list-style: none;
  }
  .contact li { display: flex; gap: 14px; color: var(--ink-grey); }
  .contact .label { width: 12px; color: var(--brand-blue); }
</style>
</head>
<body>
<main class="canvas">

  <section class="card card-back" aria-label="Card back">
    <svg class="facets" width="680" height="388" viewBox="0 0 680 388" aria-hidden="true">
      <rect x="300" y="0" width="380" height="210" fill="#ffffff" opacity="0.05"/>
      <rect x="120" y="120" width="420" height="268" fill="#ffffff" opacity="0.05"/>
      <rect x="0" y="250" width="160" height="138" fill="#000000" opacity="0.05"/>
    </svg>
    <div class="back-name">Tim Halvarsen</div>
    <div class="back-tagline">Numeric Insight Services</div>
  </section>

  <section class="card card-front" aria-label="Card front">
    <svg class="edge-notch" width="26" height="40" viewBox="0 0 26 40" aria-hidden="true">
      <polygon points="0,0 26,20 0,40" fill="var(--brand-blue)"/>
    </svg>

    <div class="credential">
      <div class="mark"><span class="dot"></span>DCred</div>
      <div class="caption">Licensed Numeric Examiner</div>
    </div>

    <div class="firm">
      <div class="firm-name">Tim Halvarsen</div>
      <div class="firm-tagline">Numeric Insight Services</div>
    </div>

    <div class="divider"></div>

    <div class="address">
      47 Harbor Lane<br>
      Brookvale, Maine<br>
      04011
    </div>

    <div class="person">
      <div class="person-name">Tim Halvarsen</div>
      <div class="person-role">managing director</div>
    </div>

    <ul class="contact">
      <li><span class="label">P</span>207 418 62 90</li>
      <li><span class="label">E</span>info@timhalvarsen.com</li>
      <li><span class="label">W</span>www.timhalvarsen.com</li>
    </ul>
  </section>

</main>
</body>
</html>
```